Business Card/Email Signature design

We need an new business card design for our business as well as an animated email signature design.<br/>Business Card:<br/>The business card designs need to have the following information for each director:<br/>Glen Purvis<br/>Managing Director<br/>glen@fernloxstaffing.com.au<br/>0468203917<br/>www.fernloxstaffing.com.au<br/><br/>and<br/><br/>Rosalind Tremby<br/>Director<br/>rosalind@fernloxstaffing.com.au<br/>0457390264<br/>www.fernloxstaffing.com.au<br/><br/>I will upload the Fernlox. Staffing logo designs to be used for the design. Our colours are black and white. I would like to see the designs in both coloured backgrounds.<br/><br/>For the email signature we need the same information. I also need to add a logo of our association NPLB of which i will add the logo as well. This NPLB logo does not need to be used for the business card unless it works with the design.<br/>For the animation part of the logo our company is called Fernlox. Staffing - We have a number of divisions called Fernlox. Construct, Fernlox. Property, Fernlox. Sales, Fernlox. Executive Support, Fernlox. Private PA, Fernlox. Talent and Fernlox. Coaching<br/>I would like for the email Signature to be designed so that the Fernlox. stays still but the words Construct, Property, Sales, Executive Support, Private PA, Talent and Coaching rotate through to capture attention and tell the story of what we do.<br/><br/>Any questions please don't hesitate to message me.

Industry/Entity Type

Recruiter

Contact Information for Business Card

Glen Purvis
Managing Director
glen@fernloxstaffing.com.au
0468203917
www.fernloxstaffing.com.au

Rosalind Tremby
Director
rosalind@fernloxstaffing.com.au
0457390264
www.fernloxstaffing.com.au

Font styles to use
Serif

Colors

Designer to choose colors to be used in the design.

Requirements
Must have
• The animation for the email signature as described
Should not have
• Any changes to my logo. Any colour other that black or white

```html
<!DOCTYPE html>
<html lang="en">
<head>
<meta charset="utf-8">
<title>Fernlox. Staffing – Business Cards</title>
<link href="https://fonts.googleapis.com/css2?family=Cormorant+Garamond:wght@600&family=Roboto:wght@400&family=Montserrat:wght@400&display=swap" rel="stylesheet">
<style>
  :root {
    --backdrop: #a4a4a4;
    --ink: #0c0c0c;
    --ink-soft: #121212;
    --paper: #ffffff;
    --on-dark: #ffffff;
    --on-dark-muted: #e4e4e4;
    --on-light: #111111;
    --on-light-muted: #4a4a4a;
    --rule-dark: #9a9a9a;
    --rule-light: #111111;
  }
  * { margin: 0; padding: 0; box-sizing: border-box; }
  html, body { width: 1200px; height: 596px; overflow: hidden; background: var(--backdrop); }
  .sheet { position: relative; width: 1200px; height: 596px; }

  .card { position: absolute; width: 400px; height: 228px; overflow: hidden; }
  .card--front-a { left: 171px; top: 60px; }
  .card--front-b { left: 627px; top: 60px; }
  .card--back-dark { left: 171px; top: 311px; background: var(--ink-soft); color: var(--on-dark); }
  .card--back-light { left: 627px; top: 311px; background: var(--paper); color: var(--on-light); }

  .card__texture { position: absolute; inset: 0; background: linear-gradient(160deg, #141414, #080808 60%, #111111); }

  .brand {
    position: absolute; left: 0; right: 0; top: 98px;
    display: flex; align-items: center; justify-content: center; gap: 12px;
  }
  .brand__mark { width: 14px; height: 14px; background: var(--on-dark); }
  .brand__name {
    font-family: "Cormorant Garamond", serif; font-weight: 600;
    font-size: 27px; letter-spacing: 1.5px; color: var(--on-dark); line-height: 1;
  }

  .back-brand {
    position: absolute; left: 48px; width: 136px; top: 100px;
    text-align: center;
    font-family: "Cormorant Garamond", serif; font-weight: 600;
    font-size: 30px; line-height: 1; letter-spacing: 0.5px;
  }
  .card--back-dark .back-brand { color: var(--on-dark); }
  .card--back-light .back-brand { color: var(--on-light); }

  .divider { position: absolute; left: 200px; top: 59px; width: 1px; height: 110px; }
  .card--back-dark .divider { background: var(--rule-dark); }
  .card--back-light .divider { background: var(--rule-light); }

  .contact { position: absolute; left: 205px; top: 69px; }
  .contact__name { font-family: "Roboto", sans-serif; font-size: 16px; line-height: 18px; }
  .contact__role { font-family: "Roboto", sans-serif; font-size: 10.5px; margin-top: 3px; }
  .card--back-dark .contact__role { color: var(--on-dark-muted); }
  .card--back-light .contact__role { color: var(--on-light-muted); }
  .contact__list { list-style: none; margin-top: 12px; }
  .contact__item {
    display: flex; align-items: center; gap: 6px; height: 14.5px;
    font-family: "Montserrat", sans-serif; font-size: 10px; white-space: nowrap;
  }
  .contact__icon { width: 10px; height: 10px; flex: none; fill: currentColor; }
</style>
</head>
<body>
<main class="sheet">
  <section class="card card--front-a">
    <div class="card__texture" role="img" aria-label="Subtle dark repeating brand pattern"></div>
    <div class="brand"><span class="brand__mark"></span><span class="brand__name">FERNLOX. STAFFING</span></div>
  </section>

  <section class="card card--front-b">
    <div class="card__texture" role="img" aria-label="Subtle dark repeating brand pattern"></div>
    <div class="brand"><span class="brand__mark"></span><span class="brand__name">FERNLOX. STAFFING</span></div>
  </section>

  <section class="card card--back-dark">
    <div class="back-brand">Fernlox.</div>
    <div class="divider"></div>
    <div class="contact">
      <p class="contact__name">GLEN PURVIS</p>
      <p class="contact__role">Managing Director</p>
      <ul class="contact__list">
        <li class="contact__item"><svg class="contact__icon" viewBox="0 0 24 24"><path d="M6.6 10.8a15 15 0 0 0 6.6 6.6l2.2-2.2a1 1 0 0 1 1-.25 11.4 11.4 0 0 0 3.6.57 1 1 0 0 1 1 1V20a1 1 0 0 1-1 1A17 17 0 0 1 3 4a1 1 0 0 1 1-1h3.5a1 1 0 0 1 1 1c0 1.25.2 2.45.57 3.57a1 1 0 0 1-.25 1z"/></svg>0468203917</li>
        <li class="contact__item"><svg class="contact__icon" viewBox="0 0 24 24"><path d="M2 5h20v14H2z M2 5l10 8 10-8" fill="none" stroke="currentColor" stroke-width="2"/></svg>glen@fernloxstaffing.com.au</li>
        <li class="contact__item"><svg class="contact__icon" viewBox="0 0 24 24"><circle cx="12" cy="12" r="10" fill="none" stroke="currentColor" stroke-width="2"/><path d="M2 12h20M12 2c3 3 3 17 0 20M12 2c-3 3-3 17 0 20" fill="none" stroke="currentColor" stroke-width="1.6"/></svg>www.fernloxstaffing.com.au</li>
      </ul>
    </div>
  </section>

  <section class="card card--back-light">
    <div class="back-brand">Fernlox.</div>
    <div class="divider"></div>
    <div class="contact">
      <p class="contact__name">GLEN PURVIS</p>
      <p class="contact__role">Managing Director</p>
      <ul class="contact__list">
        <li class="contact__item"><svg class="contact__icon" viewBox="0 0 24 24"><path d="M6.6 10.8a15 15 0 0 0 6.6 6.6l2.2-2.2a1 1 0 0 1 1-.25 11.4 11.4 0 0 0 3.6.57 1 1 0 0 1 1 1V20a1 1 0 0 1-1 1A17 17 0 0 1 3 4a1 1 0 0 1 1-1h3.5a1 1 0 0 1 1 1c0 1.25.2 2.45.57 3.57a1 1 0 0 1-.25 1z"/></svg>0468203917</li>
        <li class="contact__item"><svg class="contact__icon" viewBox="0 0 24 24"><path d="M2 5h20v14H2z M2 5l10 8 10-8" fill="none" stroke="currentColor" stroke-width="2"/></svg>glen@fernloxstaffing.com.au</li>
        <li class="contact__item"><svg class="contact__icon" viewBox="0 0 24 24"><circle cx="12" cy="12" r="10" fill="none" stroke="currentColor" stroke-width="2"/><path d="M2 12h20M12 2c3 3 3 17 0 20M12 2c-3 3-3 17 0 20" fill="none" stroke="currentColor" stroke-width="1.6"/></svg>www.fernloxstaffing.com.au</li>
      </ul>
    </div>
  </section>
</main>
</body>
</html>
```